New Corporate Business Card - Velmorana

What we need:
We need a new corporate business card.
We want a new template that we can change by ourself.
We want business card modern and minimalist but that looks professional.
We will print it in 300 gr soft-touch.
Why not a white side with the logo and a red/grey side with the content?
Why not a grey side and a red side like our logo?
I am sure that you have better idea than ours that's the reason we come here.

Who we are:
We are a private label company in cosmetics based in Switzerland. We work in BtoB. We make skin care products for other brands.

Target Market(s)

B to B - Worldwide - any gender

Industry/Entity Type

Cosmetics

Contact Information for Business Card

Side 1:
Logo
Your Swiss Private Label Manufacturer or www.velmorana-example.ch

Side 2:
Name and surname (Example: Lucien Marchetaz)
Job Description (General Manager)
Telephone (+41 32 915 63 00)
Direct (+41 32 915 63 63)
Email (lucien.marchetaz@velmorana-example.ch)
Chemin des Pélerines 14, 2000 Neuchâtel, Switzerland
www.velmorana-example.ch

Font styles to use
Serif
Sans Serif

Requirements
Must have
• You can use 4 colors: white, red, grey and/or black .
Should not have
• Too much colors, too much things. We want it simple!

```html
<!DOCTYPE html>
<html lang="en">
<head>
<meta charset="utf-8">
<title>Velmorana – Business Card</title>
<link rel="stylesheet" href="https://fonts.googleapis.com/css2?family=Questrial&display=swap">
<style>
  :root {
    --red: #e01f1c;
    --grey: #a7a8aa;
    --grey-dark: #555659;
    --white: #ffffff;
    --backdrop: #e9e9ea;
    --card-w: 640px;
    --card-h: 366px;
  }
  * { box-sizing: border-box; margin: 0; padding: 0; }
  html, body {
    width: 1200px; height: 858px; overflow: hidden;
    background: var(--backdrop);
    font-family: "Questrial", "Century Gothic", sans-serif;
  }
  .stage {
    width: 1200px; height: 858px;
    display: flex; flex-direction: column;
    align-items: center; justify-content: space-evenly;
  }
  .card {
    position: relative;
    width: var(--card-w); height: var(--card-h);
    overflow: hidden;
    box-shadow: 0 6px 18px rgba(0,0,0,.18);
  }

  /* Front side */
  .card--front { background: var(--red); color: var(--white); }
  .brand {
    position: absolute; left: 50%; transform: translateX(-50%);
    display: flex; align-items: center; gap: 14px;
    letter-spacing: 6px; text-transform: uppercase; white-space: nowrap;
  }
  .card--front .brand { top: 110px; font-size: 40px; color: var(--white); }
  .brand__square { width: 22px; height: 22px; background: var(--grey); flex: none; }
  .address {
    position: absolute; left: 44px; bottom: 40px;
    display: flex; align-items: center; gap: 10px;
    font-size: 15px; letter-spacing: .3px;
  }
  .address svg { width: 18px; height: 22px; flex: none; }

  /* Back side */
  .card--back { background: var(--white); color: var(--grey-dark); }
  .card--back .brand { top: 34px; font-size: 28px; color: var(--red); letter-spacing: 5px; }
  .card--back .brand__square { width: 16px; height: 16px; }
  .identity {
    position: absolute; left: 0; right: 0; top: 112px; height: 60px;
  }
  .identity__name {
    position: absolute; left: 50%; transform: translateX(-50%); top: 0;
    font-size: 28px; color: var(--red); letter-spacing: .5px; white-space: nowrap;
  }
  .identity__role {
    position: absolute; left: 50%; transform: translateX(-50%); top: 36px;
    font-size: 16px; color: var(--grey-dark); letter-spacing: .8px; white-space: nowrap;
  }
  .rule { position: absolute; height: 1px; background: var(--grey-dark); opacity: .6; }
  .rule--left { left: 28px; width: 190px; top: 20px; }
  .rule--right { right: 28px; width: 190px; top: 46px; }

  .contacts {
    position: absolute; left: 28px; right: 28px; top: 204px;
    display: flex; justify-content: space-between;
  }
  .contact {
    display: flex; flex-direction: column; align-items: center; gap: 8px;
    font-size: 14px; color: var(--grey-dark); white-space: nowrap;
  }
  .contact svg { width: 18px; height: 18px; }

  .footer-band {
    position: absolute; left: 0; right: 0; bottom: 28px; height: 30px;
    background: var(--grey);
  }
  .website {
    position: absolute; left: 50%; transform: translateX(-50%); bottom: 28px;
    height: 30px; padding: 0 34px;
    background: var(--red); color: var(--white);
    font-size: 15px; line-height: 30px; letter-spacing: .5px; white-space: nowrap;
  }
</style>
</head>
<body>
<main class="stage">

  <section class="card card--front" aria-label="Business card front">
    <div class="brand"><span class="brand__square"></span><span>Velmorana</span></div>
    <p class="address">
      <svg viewBox="0 0 18 22" aria-hidden="true">
        <path d="M9 1a6 6 0 0 0-6 6c0 4.5 6 10 6 10s6-5.5 6-10a6 6 0 0 0-6-6z" fill="none" stroke="#fff" stroke-width="1.8"/>
        <circle cx="9" cy="7" r="2" fill="#fff"/>
        <ellipse cx="9" cy="19.5" rx="7" ry="1.6" fill="none" stroke="#fff" stroke-width="1.4"/>
      </svg>
      Chemin des Pélerines 14, 2000 Neuchâtel, Switzerland
    </p>
  </section>

  <section class="card card--back" aria-label="Business card back">
    <div class="brand"><span class="brand__square"></span><span>Velmorana</span></div>

    <div class="identity">
      <span class="rule rule--left"></span>
      <h1 class="identity__name">RÉMY FALQUET</h1>
      <p class="identity__role">General Manager</p>
      <span class="rule rule--right"></span>
    </div>

    <ul class="contacts" style="list-style:none">
      <li class="contact">
        <svg viewBox="0 0 18 18" aria-hidden="true">
          <rect x="5" y="1" width="8" height="16" rx="1.5" fill="none" stroke="#e01f1c" stroke-width="1.6"/>
          <line x1="5" y1="13.5" x2="13" y2="13.5" stroke="#e01f1c" stroke-width="1.2"/>
        </svg>
        +41 32 915 63 63
      </li>
      <li class="contact">
        <svg viewBox="0 0 18 18" aria-hidden="true">
          <path d="M4 2l3 3-2 2c1 2.5 3.5 5 6 6l2-2 3 3-2 2C8 16 2 10 2 4z" fill="#e01f1c"/>
        </svg>
        +41 32 915 63 00
      </li>
      <li class="contact">
        <svg viewBox="0 0 18 18" aria-hidden="true">
          <rect x="1" y="4" width="16" height="11" fill="#e01f1c"/>
          <path d="M1 4l8 6 8-6" fill="none" stroke="#fff" stroke-width="1.3"/>
        </svg>
        lucien.marchetaz@velmorana-example.ch
      </li>
    </ul>

    <div class="footer-band"></div>
    <p class="website">www.velmorana-example.ch</p>
  </section>

</main>
</body>
</html>
```